Wellmere Talking Therapies House

We need a design for magazine advert, ideally high resolution to advertise our counselling centre. we would like this to include a photo of two people talking, as if in a counselling session. See our logo and colour range on our website. www.wellmere-house.co.uk
The photo should not include cups of coffee, clipboards, desks, people touching. it needs to be two people in armchairs sympathetically listening and looking at each other.
The font type is Great Vibes on the logo. Our design should communicate a centre of excellence delivering high quality, professional services in stylishly furnished surroundings.
Updates

Hello Everyone We have had a number of designs that look quite promising but are missing the brief. Can I reiterate that we need a photograph of 2 people seated talking to each other in a sincere way. There shouldn't be office chairs but comfortable chairs. There should be no physical contact. There should be no clipboards.Thank you very muchHeather Added Sunday, March 12, 2017

Target Market(s)

people seeking counselling and psychotherapy

Font styles to use
Other font styles liked:
• Great Vibes as in our logo for some of the print. See attached file.

Requirements
Must have
• good photograph
• Two high res Pixelvane photos:
• https://pixelvane-files.example-portal.net/download/photo-one-ref-7341
• https://pixelvane-files.example-portal.net/download/photo-two-ref-9826
Nice to have
• Watermark in keeping with our logo.
Should not have
• Darkness

```html
<!DOCTYPE html>
<html lang="en">
<head>
<meta charset="utf-8">
<title>Wellmere Talking Therapies House – Magazine Advert</title>
<link rel="stylesheet" href="https://fonts.googleapis.com/css2?family=Great+Vibes&family=Montserrat:wght@400;500;600&display=swap">
<style>
  :root{
    --page-bg:#ffffff;
    --cream:#f1ebdc;
    --sage:#a8bb84;
    --olive:#8a9a3c;
    --phone-green:#8fae78;
    --brown:#3b2f2c;
    --ink:#2e2523;
    --text:#3a3330;
    --white:#ffffff;
  }
  html,body{margin:0;width:1200px;height:1200px;overflow:hidden;background:var(--page-bg);}
  .stage{position:relative;width:1200px;height:1200px;}
  .advert{
    position:absolute;left:198px;top:30px;width:777px;height:1100px;
    transform:scale(1.036);transform-origin:0 0;
    background:var(--cream);overflow:hidden;
    box-shadow:0 14px 40px rgba(0,0,0,.12);
    font-family:"Montserrat",Arial,sans-serif;color:var(--text);
  }
  .advert__shapes{position:absolute;inset:0;width:777px;height:1100px;}
  .headline{
    position:absolute;left:0;width:777px;top:500px;margin:0;text-align:center;
    font-family:"Great Vibes",cursive;font-weight:400;color:var(--ink);
    font-size:49px;line-height:58px;
  }
  .headline span{display:block;}
  .headline .line-two{padding-right:20px;}
  .intro{
    position:absolute;left:162px;top:664px;width:330px;margin:0;
    font-size:16.5px;line-height:23px;
  }
  .intro strong{color:var(--olive);font-weight:600;}
  .contact{position:absolute;left:63px;top:912px;color:var(--white);}
  .contact__hours{margin:0;font-size:14.5px;line-height:17px;}
  .contact__phone{margin:2px 0 10px;font-size:31px;line-height:36px;color:var(--phone-green);font-weight:400;letter-spacing:.5px;}
  .contact__address{margin:0 0 20px;font-size:14px;line-height:17px;font-style:normal;}
  .contact__web{margin:0;font-size:15px;font-weight:600;}
  .brand{position:absolute;left:380px;top:900px;width:334px;text-align:center;}
  .brand__dot{width:52px;height:52px;border-radius:50%;background:var(--sage);margin:0 auto 14px;}
  .brand__name{margin:0;font-family:"Great Vibes",cursive;font-weight:400;font-size:33px;line-height:36px;color:var(--ink);}
</style>
</head>
<body>
<div class="stage">
  <article class="advert">
    <svg class="advert__shapes" viewBox="0 0 777 1100">
      <defs>
        <linearGradient id="roomTones" x1="0" y1="0" x2="1" y2="0.35">
          <stop offset="0" stop-color="#f3f0ea"/>
          <stop offset="0.16" stop-color="#e7d9c4"/>
          <stop offset="0.3" stop-color="#b3c9dc"/>
          <stop offset="0.46" stop-color="#a4673c"/>
          <stop offset="0.6" stop-color="#dcd8cf"/>
          <stop offset="0.78" stop-color="#f4f2ee"/>
          <stop offset="1" stop-color="#9eb3cf"/>
        </linearGradient>
        <linearGradient id="roomFloor" x1="0" y1="0" x2="0" y2="1">
          <stop offset="0.45" stop-color="#000" stop-opacity="0"/>
          <stop offset="1" stop-color="#5a3f2c" stop-opacity="0.35"/>
        </linearGradient>
        <linearGradient id="pairTones" x1="0" y1="0" x2="1" y2="0">
          <stop offset="0" stop-color="#eeece8"/>
          <stop offset="0.45" stop-color="#e4c4b8"/>
          <stop offset="0.7" stop-color="#d9cfc8"/>
          <stop offset="1" stop-color="#a9d3c6"/>
        </linearGradient>
      </defs>
      <g class="photo-session" role="img" aria-label="Photo: counsellor and client seated in armchairs talking in a bright, furnished room">
        <path fill="url(#roomTones)" d="M0 0H777V262C700 350 560 420 400 455C250 488 100 505 0 558Z"/>
        <path fill="url(#roomFloor)" d="M0 0H777V262C700 350 560 420 400 455C250 488 100 505 0 558Z"/>
      </g>
      <path class="curve-accent" fill="#a8bb84" d="M500 458C630 430 730 360 777 280V256C720 343 630 418 500 458Z"/>
      <path class="photo-pair" role="img" aria-label="Photo: two smiling women seated together in a calm consulting room"
            fill="url(#pairTones)" d="M420 836C470 760 530 690 610 650C665 626 720 618 777 612V725C700 770 600 818 500 834Z"/>
      <path class="panel-contact" fill="#3b2f2c" d="M0 1100V905Q0 833 75 832L420 830V1100Z"/>
      <path class="panel-brand" fill="#ffffff" d="M318 1100C330 960 370 850 440 836C560 830 690 790 777 722V1100Z"/>
    </svg>

    <h1 class="headline">
      <span class="line-one">Confidential Therapeutic Services</span>
      <span class="line-two">in the Heart of Old Town</span>
    </h1>

    <p class="intro">We have over <strong>30 carefully selected, qualified and professional therapists</strong> offering a range of services to help individuals, families and couples.</p>

    <div class="contact">
      <p class="contact__hours">Appointments available<br>throughout the day and evening</p>
      <p class="contact__phone">01632 960418</p>
      <address class="contact__address">8 Linden Row, Old Town,<br>Ashcombe AC4 2LD</address>
      <p class="contact__web">www.wellmere-house.co.uk</p>
    </div>

    <div class="brand">
      <div class="brand__dot"></div>
      <p class="brand__name">Wellmere Talking Therapies House</p>
    </div>
  </article>
</div>
</body>
</html>
```